Communication Skill: NODE Assist

I need a Design for a skill I teach to youth. That's why the title NODE Assist. NODE stands for Thoughts, Emotions, Concerns, Hopes & Desires. Under each word are some examples that are meant to help people discuss certain things. I tried to create something myself but want something much more creative and dynamic. I have attached what I designed because it has the information I need in the design. Want it to have a techie look to it.

```html
<!DOCTYPE html>
<html lang="en">
<head>
<meta charset="utf-8">
<title>NODE Assist</title>
<link rel="stylesheet" href="https://fonts.googleapis.com/css2?family=Bitter:wght@800&family=Montserrat:wght@500;600&display=swap">
<style>
  :root {
    --ink: #231f20;
    --title-ink: #3b2f25;
    --orange-light: #fbb31b;
    --orange-dark: #f15a24;
    --orange-letter: #f0861f;
    --purple-dark: #9b2a8c;
    --purple-light: #d4509a;
    --purple-letter: #c0288c;
    --lime: #a6ce39;
    --yellow: #d9e021;
    --green-letter: #7ab51d;
    --teal-light: #7cc5b4;
    --blue: #0a8cc7;
    --teal-letter: #1fb1bf;
    --gear-shade: #d1d3d4;
    --gear-light: #f5f5f5;
    --white: #ffffff;
  }
  html, body {
    margin: 0;
    padding: 0;
    overflow: hidden;
    background: var(--white);
  }
  .canvas {
    position: relative;
    width: 1200px;
    height: 1080px;
    overflow: hidden;
    background: var(--white);
  }
  .artwork {
    position: absolute;
    inset: 0;
  }
  .title {
    position: absolute;
    top: 62px;
    left: 0;
    width: 1200px;
    margin: 0;
    text-align: center;
    font-family: "Bitter", "Rockwell", serif;
    font-weight: 800;
    font-size: 76px;
    line-height: 1;
    letter-spacing: 2px;
    color: var(--title-ink);
  }
  .quadrant {
    position: absolute;
    width: 409px;
    height: 409px;
    text-align: center;
    color: var(--ink);
  }
  .quadrant--thoughts { left: 168px; top: 183px; }
  .quadrant--emotions { left: 583px; top: 183px; }
  .quadrant--concerns { left: 168px; top: 596px; }
  .quadrant--hopes    { left: 583px; top: 596px; }

  .initial {
    position: absolute;
    left: 0;
    width: 100%;
    margin: 0;
    font-family: "Bitter", "Rockwell", serif;
    font-weight: 800;
    font-size: 104px;
    line-height: 1;
  }
  .heading {
    position: absolute;
    left: 0;
    width: 100%;
    margin: 0;
    font-family: "Montserrat", "Arial", sans-serif;
    font-weight: 600;
    font-size: 38px;
    line-height: 1;
    letter-spacing: 0.5px;
  }
  .prompts {
    position: absolute;
    left: 40px;
    width: 329px;
    margin: 0;
    padding: 0;
    list-style: none;
    font-family: "Montserrat", "Arial", sans-serif;
    font-weight: 500;
    font-size: 19px;
    line-height: 27px;
    word-spacing: 2px;
  }
  .quadrant--thoughts .initial,
  .quadrant--emotions .initial { top: 50px; }
  .quadrant--thoughts .heading,
  .quadrant--emotions .heading { top: 160px; }
  .quadrant--thoughts .prompts,
  .quadrant--emotions .prompts { top: 206px; }

  .quadrant--concerns .initial,
  .quadrant--hopes .initial { top: 70px; }
  .quadrant--concerns .heading,
  .quadrant--hopes .heading { top: 173px; }
  .quadrant--concerns .prompts,
  .quadrant--hopes .prompts { top: 218px; }

  .quadrant--thoughts .initial { color: var(--orange-letter); }
  .quadrant--emotions .initial { color: var(--purple-letter); }
  .quadrant--concerns .initial { color: var(--green-letter); }
  .quadrant--hopes .initial    { color: var(--teal-letter); }

  .gear-body { fill: url(#gearFill); }
  .gear-teeth {
    fill: none;
    stroke: url(#gearFill);
    stroke-width: 22;
    stroke-dasharray: 26 30.55;
  }
  .gears { filter: drop-shadow(0 2px 3px rgba(0,0,0,0.18)); }
  .icon-white { fill: var(--white); }
  .icon-ring { fill: none; stroke: var(--white); stroke-width: 3.5; }
</style>
</head>
<body>
<div class="canvas">
  <svg class="artwork" width="1200" height="1080" viewBox="0 0 1200 1080" aria-hidden="true">
    <defs>
      <linearGradient id="petalOrange" x1="0" y1="0" x2="1" y2="1">
        <stop offset="0" stop-color="var(--orange-light)"/>
        <stop offset="1" stop-color="var(--orange-dark)"/>
      </linearGradient>
      <linearGradient id="petalPurple" x1="0" y1="0" x2="1" y2="1">
        <stop offset="0" stop-color="var(--purple-dark)"/>
        <stop offset="1" stop-color="var(--purple-light)"/>
      </linearGradient>
      <linearGradient id="petalLime" x1="0" y1="0" x2="1" y2="0.4">
        <stop offset="0" stop-color="var(--lime)"/>
        <stop offset="1" stop-color="var(--yellow)"/>
      </linearGradient>
      <linearGradient id="petalBlue" x1="0" y1="0.3" x2="1" y2="0.7">
        <stop offset="0" stop-color="var(--teal-light)"/>
        <stop offset="1" stop-color="var(--blue)"/>
      </linearGradient>
      <linearGradient id="gearFill" x1="0" y1="0" x2="1" y2="0">
        <stop offset="0" stop-color="var(--gear-shade)"/>
        <stop offset="1" stop-color="var(--gear-light)"/>
      </linearGradient>
    </defs>

    <g class="petals">
      <path d="M577 592 H372.5 A204.5 204.5 0 0 1 168 387.5 A204.5 204.5 0 0 1 372.5 183 A204.5 204.5 0 0 1 577 387.5 Z" fill="url(#petalOrange)"/>
      <path d="M583 592 V387.5 A204.5 204.5 0 0 1 787.5 183 A204.5 204.5 0 0 1 992 387.5 A204.5 204.5 0 0 1 787.5 592 Z" fill="url(#petalPurple)"/>
      <path d="M577 596 V800.5 A204.5 204.5 0 0 1 372.5 1005 A204.5 204.5 0 0 1 168 800.5 A204.5 204.5 0 0 1 372.5 596 Z" fill="url(#petalLime)"/>
      <path d="M583 596 H787.5 A204.5 204.5 0 0 1 992 800.5 A204.5 204.5 0 0 1 787.5 1005 A204.5 204.5 0 0 1 583 800.5 Z" fill="url(#petalBlue)"/>
    </g>

    <g class="gears">
      <circle class="gear-teeth" cx="372.5" cy="387.5" r="162"/>
      <circle class="gear-body" cx="372.5" cy="387.5" r="153"/>
      <circle class="gear-teeth" cx="787.5" cy="387.5" r="162"/>
      <circle class="gear-body" cx="787.5" cy="387.5" r="153"/>
      <circle class="gear-teeth" cx="372.5" cy="800.5" r="162"/>
      <circle class="gear-body" cx="372.5" cy="800.5" r="153"/>
      <circle class="gear-teeth" cx="787.5" cy="800.5" r="162"/>
      <circle class="gear-body" cx="787.5" cy="800.5" r="153"/>
    </g>

    <g class="icon-thought-cloud">
      <circle class="icon-white" cx="515" cy="546" r="13"/>
      <circle class="icon-white" cx="531" cy="538" r="17"/>
      <circle class="icon-white" cx="548" cy="546" r="13"/>
      <ellipse class="icon-white" cx="531" cy="553" rx="24" ry="10"/>
      <circle class="icon-white" cx="513" cy="568" r="4.5"/>
      <circle class="icon-white" cx="505" cy="576" r="2.8"/>
    </g>

    <g class="icon-mood" role="img" aria-label="Happy mood icon">
      <circle class="icon-ring" cx="623" cy="546" r="27"/>
    </g>
    <g class="icon-worry" role="img" aria-label="Worried mood icon">
      <circle class="icon-white" cx="523" cy="640" r="32"/>
    </g>

    <polygon class="icon-white icon-star" points="623,618 628.3,632.7 643.9,633.2 631.6,642.8 635.9,657.8 623,649 610.1,657.8 614.4,642.8 602.1,633.2 617.7,632.7"/>
  </svg>

  <h1 class="title">NODE ASSIST</h1>

  <section class="quadrant quadrant--thoughts">
    <p class="initial">T</p>
    <h2 class="heading">THOUGHTS</h2>
    <ul class="prompts">
      <li>It seems… I wonder…</li>
      <li>It’s my opinion… I believe…</li>
      <li>I assume… I think…</li>
    </ul>
  </section>

  <section class="quadrant quadrant--emotions">
    <p class="initial">E</p>
    <h2 class="heading">EMOTIONS</h2>
    <ul class="prompts">
      <li>I’m… hopeful worried sad</li>
      <li>afraid mad glad happy</li>
      <li>confident insecure lonely</li>
      <li>bothered uncertain</li>
    </ul>
  </section>

  <section class="quadrant quadrant--concerns">
    <p class="initial">C</p>
    <h2 class="heading">CONCERNS</h2>
    <ul class="prompts">
      <li>I worry about…</li>
      <li>I’m afraid that…</li>
      <li>I’m nervous because…</li>
      <li>It bothers me that…</li>
    </ul>
  </section>

  <section class="quadrant quadrant--hopes">
    <p class="initial">H</p>
    <h2 class="heading">HOPES</h2>
    <ul class="prompts">
      <li>I hope… I wish…</li>
      <li>It’s my desire…</li>
      <li>I’d like to see…</li>
      <li>I want… I need…</li>
    </ul>
  </section>
</div>
</body>
</html>
```